Business cards for the RT Group

We are looking for a template for our new business cards for our company that we can edit ourselves.
You will find our company colors in the logo. the logo on the back and on the front
first name Last Name
position
E-mail address
mobile number
landline number
Companies we have 2 RT Sicherheit GmbH and RT Services GmbH
address
Lindauer Weg 42
22543 Hamburg
www.rtverbund-beispiel.de

Something modern, simple but professional

if you have any questions, bring it on.

Industry/Entity Type

Sicherheit

Contact Information for Business Card

Steht in der Beschreibung

Colors
F0912C
F2A743
F7CA91
FBE8D2
FDF5EE

Requirements
Must have
• recognition value
Nice to have
• professional
Should not have
• Playful

```html
<!DOCTYPE html>
<html lang="de">
<head>
<meta charset="utf-8">
<title>RT Gruppe – Visitenkarten</title>
<link rel="stylesheet" href="https://fonts.googleapis.com/css2?family=Montserrat:wght@300;400;600;700&display=swap">
<style>
  :root {
    --backdrop: #222222;
    --card-white: #ffffff;
    --brand-orange: #f0811c;
    --brand-grey: #5b5b5b;
    --text-light: #ffffff;
  }
  * { margin: 0; padding: 0; box-sizing: border-box; }
  html, body {
    width: 1200px; height: 1020px; overflow: hidden;
    background: var(--backdrop);
    font-family: "Montserrat", Arial, sans-serif;
  }
  .canvas { position: relative; width: 1200px; height: 1020px; }

  .card {
    position: absolute; left: 250px; width: 700px; height: 400px;
    background: var(--card-white); overflow: hidden;
    box-shadow: 0 18px 40px rgba(0,0,0,.55);
  }
  .card--front { top: 70px; }
  .card--back { top: 540px; }

  /* Front */
  .wordmark {
    position: absolute; display: flex; align-items: center; gap: 16px;
    color: var(--brand-grey); font-weight: 700; letter-spacing: 1px;
  }
  .wordmark__mark { background: var(--brand-orange); flex: none; }
  .card--front .wordmark { left: 210px; top: 95px; font-size: 60px; }
  .card--front .wordmark__mark { width: 46px; height: 46px; }

  .front-band {
    position: absolute; left: 0; top: 268px; width: 100%; height: 70px;
    background: var(--brand-orange);
    display: flex; align-items: center; justify-content: center;
    color: var(--text-light); font-size: 26px; font-weight: 400; letter-spacing: 1px;
  }
  .front-rule {
    position: absolute; left: 0; top: 349px; width: 100%; height: 7px;
    background: var(--brand-orange);
  }

  /* Back */
  .back-shape { position: absolute; inset: 0; }
  .card--back .wordmark { left: 478px; top: 165px; font-size: 38px; }
  .card--back .wordmark__mark { width: 28px; height: 28px; }

  .contact-block { position: absolute; left: 46px; top: 78px; color: var(--text-light); }
  .person__name { font-size: 30px; font-weight: 700; letter-spacing: 1px; line-height: 1; }
  .person__role { font-size: 17px; font-weight: 300; margin-top: 4px; }
  .person__rule { width: 300px; height: 2px; background: var(--text-light); margin: 10px 0 10px; }
  .companies { font-size: 17px; font-weight: 700; line-height: 1.25; }

  .contact-list { list-style: none; margin-top: 16px; }
  .contact-list li {
    display: flex; align-items: center; gap: 12px;
    font-size: 14px; font-weight: 400; height: 32px;
  }
  .contact-list svg { width: 22px; height: 22px; flex: none; }
</style>
</head>
<body>
<main class="canvas">

  <section class="card card--front" aria-label="Visitenkarte Vorderseite">
    <div class="wordmark"><span class="wordmark__mark"></span><span>RT Gruppe</span></div>
    <div class="front-band">www.rtverbund-beispiel.de</div>
    <div class="front-rule"></div>
  </section>

  <section class="card card--back" aria-label="Visitenkarte Rückseite">
    <svg class="back-shape" viewBox="0 0 700 400" preserveAspectRatio="none" aria-hidden="true">
      <polygon points="0,0 560,0 330,400 0,400" fill="var(--brand-orange)"/>
      <polygon points="572,0 586,0 356,400 342,400" fill="var(--brand-orange)"/>
    </svg>

    <div class="wordmark"><span class="wordmark__mark"></span><span>RT Gruppe</span></div>

    <div class="contact-block">
      <p class="person__name">JONAS BERGER</p>
      <p class="person__role">Position</p>
      <div class="person__rule"></div>
      <p class="companies">RT Sicherheit GmbH &amp;<br>RT Services GmbH</p>

      <ul class="contact-list">
        <li>
          <svg viewBox="0 0 24 24" aria-hidden="true"><path d="M12 2a7 7 0 0 0-7 7c0 5 7 13 7 13s7-8 7-13a7 7 0 0 0-7-7z" fill="#fff"/><circle cx="12" cy="9" r="2.6" fill="var(--brand-orange)"/></svg>
          <span>Lindauer Weg 42, 22543 Hamburg</span>
        </li>
        <li>
          <svg viewBox="0 0 24 24" aria-hidden="true"><path d="M6.6 10.8a15 15 0 0 0 6.6 6.6l2.2-2.2a1 1 0 0 1 1-.25 11 11 0 0 0 3.6.6 1 1 0 0 1 1 1V20a1 1 0 0 1-1 1A17 17 0 0 1 3 4a1 1 0 0 1 1-1h3.5a1 1 0 0 1 1 1 11 11 0 0 0 .6 3.6 1 1 0 0 1-.25 1z" fill="#fff"/></svg>
          <span>+49 40 555 0142 | +49 171 555 0198</span>
        </li>
        <li>
          <svg viewBox="0 0 24 24" aria-hidden="true"><rect x="2" y="5" width="20" height="14" fill="#fff"/><path d="M2 5l10 8 10-8M2 19l7-7M22 19l-7-7" fill="none" stroke="var(--brand-orange)" stroke-width="1.4"/></svg>
          <span>info@rtverbund-beispiel.de</span>
        </li>
        <li>
          <svg viewBox="0 0 24 24" aria-hidden="true" fill="none" stroke="#fff" stroke-width="1.6"><circle cx="12" cy="12" r="9.5"/><ellipse cx="12" cy="12" rx="4.2" ry="9.5"/><path d="M2.5 12h19M4 7h16M4 17h16"/></svg>
          <span>www.rtverbund-beispiel.de</span>
        </li>
      </ul>
    </div>
  </section>

</main>
</body>
</html>
```